Visitenkarte erstellen für Reiki Praxis

Visitenkarten für Reiki Praxis Doppelseitig

business cards reiki practice double-sided

The background can also be a different color

```html
<!DOCTYPE html>
<html lang="de">
<head>
<meta charset="utf-8">
<title>Lumen Balance – Visitenkarte</title>
<link rel="stylesheet" href="https://fonts.googleapis.com/css2?family=Marcellus&family=Quicksand:wght@400;500&display=swap">
<style>
  :root {
    --canvas: #ffffff;
    --card: #000000;
    --ink: #ffffff;
    --accent-gold: #f0a830;
    --accent-yellow: #e8e21c;
    --accent-rose: #e8336d;
  }
  html, body {
    margin: 0;
    padding: 0;
    width: 1200px;
    height: 1000px;
    overflow: hidden;
    background: var(--canvas);
  }
  .sheet {
    position: relative;
    width: 1200px;
    height: 1000px;
  }
  .card {
    position: absolute;
    background: var(--card);
    width: 482px;
    height: 312px;
  }
  .card--front { left: 355px; top: 171px; }
  .card--back  { left: 354px; top: 517px; height: 313px; }

  .front-brand {
    position: absolute;
    left: 0; right: 0; top: 128px;
    display: flex;
    align-items: center;
    justify-content: center;
    gap: 16px;
  }
  .front-brand__dot {
    width: 26px;
    height: 26px;
    border: 2px solid var(--accent-rose);
    border-radius: 50%;
  }
  .front-brand__name {
    font-family: "Marcellus", serif;
    font-size: 38px;
    letter-spacing: 2px;
    color: var(--accent-rose);
  }

  .back-brand {
    position: absolute;
    left: 0; right: 0; top: 60px;
    display: flex;
    flex-direction: column;
    align-items: center;
  }
  .back-brand__dot {
    width: 48px;
    height: 48px;
    border: 1.5px solid var(--accent-gold);
    border-radius: 50%;
    margin-bottom: 16px;
  }
  .back-brand__name {
    font-family: "Marcellus", serif;
    font-size: 22px;
    letter-spacing: 0.5px;
    color: var(--ink);
    line-height: 1;
  }
  .back-brand__person {
    font-family: "Quicksand", sans-serif;
    font-size: 15px;
    letter-spacing: 4px;
    color: var(--accent-yellow);
    margin-top: 9px;
  }

  .contact {
    position: absolute;
    top: 228px;
    font-family: "Quicksand", sans-serif;
    font-size: 13px;
    line-height: 17px;
    color: var(--ink);
    margin: 0;
  }
  .contact--address { left: 47px; }
  .contact--reach { right: 44px; text-align: right; }
</style>
</head>
<body>
<main class="sheet">
  <section class="card card--front" aria-label="Vorderseite">
    <div class="front-brand">
      <span class="front-brand__dot"></span>
      <span class="front-brand__name">LUMEN BALANCE</span>
    </div>
  </section>

  <section class="card card--back" aria-label="Rückseite">
    <div class="back-brand">
      <span class="back-brand__dot"></span>
      <span class="back-brand__name">LUMEN BALANCE</span>
      <span class="back-brand__person">MARA VENN</span>
    </div>
    <address class="contact contact--address">
      Lindenweg 7<br>
      Hollfeld<br>
      Germany
    </address>
    <address class="contact contact--reach">
      +49 0123 45 67 89<br>
      venn@lumenbalance.example<br>
      lumenbalance.example
    </address>
  </section>
</main>
</body>
</html>
```